Whey Protein Packet Label Design

Company background:

Company name: Tidewell Form

Website: tidewellform.com

Summary: We offer single serving supplements on the go that are all natural. We are all about healthy living and portable packaging that makes it easy to drink anywhere. Our Whey Protein Packet saves time and is convenient for our customers to make a protein shake anywhere, there is no prep time, cook time, or clean up time. These protein packets can be added into any shaker and it is easily mixed, no more large bulk tubs of protein needed anymore because we offer single servings that are manageable to carry around.

Style: Our company name is Tidewell Form, so in our logo we are saying that anyone can reach the mountain peak by taking healthy foods. That somehow needs to be shown through a pattern or something.

Products: Whey Protein Packets, Energy Sticks, Recovery Sticks

Product Label Instruction:

I need a product label for the Whey Protein Packet for 5 flavors.
-There should be one generic design, and the flavors just change according to color scheme and pictures

1. Strawberry Banana Smoothie (100% Organic Fruit Powder)
color scheme: Red, white, brown
2. Peanut Butter Smoothie (100% Organic Nut Powder)
color scheme: light brown, brown, white
3. Chocolate Smoothie(100% Organic Cacao Powder)
color scheme: dark brown, brown, white
4. Vanilla Shake (100% Pure Vanilla Powder)
color scheme: light cream, brown, white
5. Banana Peanut Butter Shake (100% Organic Fruit & Nut Powder)
color scheme: yellow, brown, white

Each flavor label design should have this text/information on the front:

1. Logo (attached) - does not need to be main part of design( just placed somewhere is fine)
2. Natural Whey Protein Packet (product title)
3. Flavor Name
4. Flavor Picture
5. 30G (amount of protein in each packet)
6. 4 professional stamps that easily state (attached an image for example)
1. Non GMO
2. Gluten Free
3. Lactose Free
4. No Artificial Flavoring
7. Net Weight 36G

Colors: I would like to use flavor color, brown, and white mainly for the packaging but I am open to different colors for diff flavors and colorful pictures.

Ideas: Please give me multiple designs to look at for the first draft.

Other company examples: I have attached some pictures of other packaging designs that I like that you can keep in mind.

Target Market(s)

Upscale, organic lifestyle, vegans, on the go people, police force, outdoor people, health junkies, gym goers, men and women

I hope you can make something that will appeal to most or all of these categories.

Industry/Entity Type

It Company

Requirements
Must have
• label dimensions: 3 x 3.75
• font: Unique, not something basic that looks like it came off of word document. It needs to look professional and unique that the upscale market would like.
Nice to have
• I have attached some examples of other companies that I like the look of. That is the type of style I am going for.
Should not have
• It should not be a basic design that I can make myself. I am looking for a professional who can make the product look like an organic style and shows that we offer HIGH QUALITY, high end supplements.

```html
<!DOCTYPE html>
<html lang="en">
<head>
<meta charset="UTF-8">
<title>Tidewell Form – Natural Whey Protein Packet</title>
<link href="https://fonts.googleapis.com/css2?family=Baloo+2:wght@500;700;800&display=swap" rel="stylesheet">
<style>
  :root {
    --backdrop: #d9d9d9;
    --label-white: #f4f3f2;
    --flavor-pink: #e98e8c;
    --brand-red: #c3101d;
    --banana-gold: #d69a17;
    --cocoa: #2a1512;
    --summit-brown: #3a211c;
    --fruit-red: #c83a33;
    --fruit-yellow: #eccb5c;
  }
  * { margin: 0; padding: 0; box-sizing: border-box; }
  html, body {
    width: 1200px; height: 960px; overflow: hidden;
    background: var(--backdrop);
    font-family: "Baloo 2", sans-serif;
  }
  .label {
    position: absolute; left: 290px; top: 30px;
    width: 620px; height: 900px;
    background: var(--label-white);
    overflow: hidden;
  }
  .side-curves { position: absolute; inset: 0; }
  .brand {
    position: absolute; top: 30px; left: 0; width: 100%;
    display: flex; justify-content: center; align-items: center; gap: 10px;
    color: var(--brand-red); font-weight: 500; font-size: 40px; letter-spacing: 3px;
  }
  .brand-dot { width: 14px; height: 14px; border-radius: 50%; background: var(--brand-red); }
  .product-title {
    position: absolute; top: 128px; left: 0; width: 100%; text-align: center;
    font-weight: 800; font-size: 40px; color: var(--cocoa);
    text-shadow: 0 0 3px #fff, 0 0 3px #fff, 0 0 3px #fff;
  }
  .flavor { position: absolute; left: 0; width: 100%; text-align: center; font-weight: 800; font-size: 37px; line-height: 1; }
  .flavor-strawberry { top: 222px; color: var(--brand-red); }
  .flavor-banana { top: 270px; color: var(--banana-gold); }
  .flavor-smoothie { top: 318px; color: var(--cocoa); }
  .fruit-picture {
    position: absolute; left: 150px; top: 372px; width: 300px; height: 224px;
    background:
      radial-gradient(ellipse 45% 38% at 55% 38%, var(--fruit-yellow) 0 55%, transparent 100%),
      radial-gradient(ellipse 55% 30% at 50% 78%, var(--fruit-red) 0 50%, transparent 100%);
  }
  .summit-scene {
    position: absolute; left: 28px; top: 560px; width: 212px; height: 340px;
    background: radial-gradient(ellipse 75% 70% at 45% 100%, var(--summit-brown) 0 45%, rgba(58,33,28,0.55) 70%, transparent 100%);
  }
  .protein-amount {
    position: absolute; top: 628px; left: 198px; width: 230px; text-align: center;
    font-weight: 800; font-size: 33px; color: var(--brand-red);
  }
  .source-note {
    position: absolute; top: 696px; left: 214px; width: 192px; text-align: center;
    font-weight: 700; font-size: 16px; line-height: 1.25; color: var(--cocoa);
  }
  .net-weight {
    position: absolute; top: 612px; left: 470px; width: 90px; text-align: center;
    color: var(--brand-red); font-weight: 800; line-height: 1;
  }
  .net-weight small { display: block; font-size: 9px; color: var(--cocoa); }
  .net-weight span { font-size: 20px; }
  .free-from { position: absolute; left: 428px; top: 707px; width: 128px; height: 134px; }
</style>
</head>
<body>
  <main class="label">
    <svg class="side-curves" width="620" height="900" viewBox="0 0 620 900" aria-hidden="true">
      <path d="M0 0 H141 C180 80 198 210 191 300 C184 420 100 520 0 580 Z" fill="var(--flavor-pink)"/>
      <path d="M620 0 H465 C432 90 420 220 426 300 C436 430 520 540 620 595 Z" fill="var(--flavor-pink)"/>
    </svg>

    <div class="brand"><span class="brand-dot"></span>Tidewell Form</div>

    <h1 class="product-title">Natural Whey Protein Packet</h1>

    <div class="flavor flavor-strawberry">Strawberry</div>
    <div class="flavor flavor-banana">Banana</div>
    <div class="flavor flavor-smoothie">Smoothie</div>

    <div class="fruit-picture" role="img" aria-label="Photo of a bunch of bananas with fresh strawberries"></div>

    <div class="summit-scene" role="img" aria-label="Silhouette illustration of a climber with raised arms standing on a mountain peak"></div>

    <div class="protein-amount">30G Protein</div>
    <p class="source-note">100%<br>Organic Fruit<br>Powder</p>

    <div class="net-weight"><small>Net Weight</small><span>40G</span></div>

    <svg class="free-from" viewBox="0 0 128 134" role="img" aria-label="Free from GMO, gluten, lactose and artificial flavoring">
      <g fill="none" stroke="var(--brand-red)" stroke-width="5">
        <circle cx="31" cy="31" r="28"/><line x1="11" y1="11" x2="51" y2="51"/>
        <circle cx="97" cy="31" r="28"/><line x1="77" y1="11" x2="117" y2="51"/>
        <circle cx="31" cy="103" r="28"/><line x1="11" y1="83" x2="51" y2="123"/>
        <circle cx="97" cy="103" r="28"/><line x1="77" y1="83" x2="117" y2="123"/>
      </g>
      <g fill="var(--brand-red)" stroke="var(--label-white)" stroke-width="2.5" paint-order="stroke" font-family="Baloo 2, sans-serif" font-weight="800" text-anchor="middle">
        <text x="31" y="36" font-size="14">GMO</text>
        <text x="97" y="35" font-size="10">GLUTEN</text>
        <text x="31" y="107" font-size="9.5">LACTOSE</text>
        <text x="97" y="101" font-size="7">ARTIFICIAL</text>
        <text x="97" y="110" font-size="7">FLAVORING</text>
      </g>
    </svg>
  </main>
</body>
</html>
```